Lantern Square, Steady Course. (Website Design)

We are launching a new bipartisan civic movement: Lantern Square. Steady Course.
The mission is this: Americans deserve a government that is legally required to serve them honestly.
We are looking for a world-class website designer capable of creating an emotionally powerful, modern, cinematic landing page experience that feels larger than politics.
This is not a campaign website for a political party or candidate. We are not looking for a red, white, and blue page with stripes, or American flags, or stock footage of smiling people in a voting booth. We are looking for an emotional and cinematic experience through and through.
The visual direction should feel:
Historic
Hopeful
American
Emotional
Cinematic
Trustworthy
Timeless
The goal is to make visitors feel that they are witnessing the beginning of something important and want to be part of it in the end.
Primary Objective:
Inspire visitors to participate in a one-minute survey and cast their vote.
The survey itself is extremely short and takes approximately one minute to complete.
Everything on the page should ultimately guide visitors toward this action while creating enough curiosity, trust, emotional engagement, and excitement that they feel compelled to take part in the movement.
Audience:
The audience is ordinary Americans across the political spectrum: Democrats, Republicans, Independents.
The design should feel unifying and welcoming.
It should avoid looking partisan, ideological, activist, or government-issued.
Creative Freedom:
We are intentionally giving designers substantial creative freedom.
We are not looking for someone to simply arrange content into predefined sections.
Instead, we are looking for a designer who can think strategically about user experience and persuasion.
The ideal design is as minimal as possible, but you may always:
Use as many sections as you believe are necessary.
Use as many images as you believe are necessary.
Include storytelling elements.
Include data visualizations.
Include timelines.
Include videos.
Include animations.
Include or exclude sections as you see fit.
Reorganize the flow entirely.
We uploaded some files containing text and section suggestions. You don’t have to use them.
We also uploaded some images to convey the general feel we’re looking for.
We are much more interested in the effectiveness of the overall experience than in any specific layout.
What success looks like:
Think outside the box.
Please do not create another generic political website. We have already explored those approaches.
We are looking for something different.
The winning design will be the one that most effectively guides visitors from curiosity to belief to participation.
When a visitor reaches the end of the experience, they should feel:
This is bigger than politics.
This is something I can support regardless of party.
This feels credible.
This feels hopeful.
I want to be part of this.
Use the survey results, the research findings, the principles, the storytelling, or any other elements you believe will help build trust and inspire participation.
Don't just impress us with flashy visuals. Impress us with a website experience that inspires people to become part of the movement and cast their vote.
The final call-to-action should feel like the natural conclusion of the journey, not a request for engagement.
Our goal is not simply to inform visitors. Our goal is to inspire them to cast their vote.
Prioritize emotional impact, storytelling, clarity, and persuasion over decorative design elements.
Final words:
Design a website experience that successfully inspires visitors to take the survey and cast their vote.
Think like a storyteller, not just a designer.
Thank you for your interest in the project.
Best of luck.

```html
<!DOCTYPE html>
<html lang="en">
<head>
<meta charset="utf-8">
<title>Lantern Square. Steady Course.</title>
<link rel="stylesheet" href="https://fonts.googleapis.com/css2?family=EB+Garamond:ital,wght@0,400;0,500;1,400&family=JetBrains+Mono:wght@500;600&display=swap">
<style>
  :root {
    --nav-bg: #141a27;
    --nav-line: #2a3142;
    --ink-light: #ffffff;
    --ink-muted: #d5d8de;
    --gold-faint: rgba(190, 160, 100, 0.28);
    --hero-deep: #151515;
    --hero-mid: #3b3b3b;
    --hero-light: #7a7a7a;
    --button-ink: #161b26;
  }
  * { box-sizing: border-box; margin: 0; padding: 0; }
  html, body {
    width: 1200px; height: 543px; overflow: hidden;
    background: var(--hero-deep);
  }
  .page { position: relative; width: 1200px; height: 543px; overflow: hidden; }

  .site-header {
    position: absolute; top: 0; left: 0; right: 0; height: 57px;
    background: var(--nav-bg);
    border-bottom: 1px solid var(--nav-line);
    display: flex; align-items: center;
    padding: 0 50px;
    z-index: 2;
  }
  .brand {
    font-family: "EB Garamond", serif;
    font-weight: 500;
    font-size: 17px;
    letter-spacing: -0.4px;
    color: var(--ink-light);
    text-transform: uppercase;
    white-space: nowrap;
  }
  .main-nav {
    position: absolute; left: 512px; top: 0; height: 57px;
    display: flex; align-items: center; gap: 20px;
  }
  .main-nav a, .registry-button, .hero-actions a {
    font-family: "JetBrains Mono", monospace;
    text-decoration: none;
    text-transform: uppercase;
  }
  .main-nav a {
    font-size: 8.5px; font-weight: 500;
    letter-spacing: 1.4px;
    color: var(--ink-muted);
  }
  .registry-button {
    position: absolute; right: 50px; top: 16px;
    width: 122px; height: 25px;
    border: 1px solid var(--ink-muted);
    display: flex; align-items: center; justify-content: center;
    font-size: 8.5px; font-weight: 600; letter-spacing: 1.4px;
    color: var(--ink-light);
  }

  .hero-photo {
    position: absolute; top: 57px; left: 0; right: 0; bottom: 0;
    background:
      radial-gradient(ellipse 55% 45% at 50% 25%, var(--hero-light) 0%, transparent 70%),
      radial-gradient(ellipse 30% 35% at 80% 15%, #8a8a8a 0%, transparent 70%),
      radial-gradient(ellipse 30% 35% at 20% 15%, #6a6a6a 0%, transparent 70%),
      linear-gradient(180deg, var(--hero-mid) 0%, #2c2c2c 50%, var(--hero-deep) 100%);
  }
  .hero-photo::after {
    content: ""; position: absolute; inset: 0;
    background: rgba(0,0,0,0.28);
  }

  .hero-content {
    position: absolute; top: 57px; left: 0; right: 0; bottom: 0;
    text-align: center; z-index: 1;
  }
  .hero-year {
    position: absolute; top: 37px; left: 0; right: 0;
    font-family: "EB Garamond", serif;
    font-size: 26px; letter-spacing: 10px;
    color: var(--gold-faint);
  }
  .hero-title {
    position: absolute; top: 98px; left: 0; right: 0;
    font-family: "EB Garamond", serif;
    font-weight: 500;
    font-size: 66px; line-height: 75px;
    letter-spacing: -1.5px;
    color: var(--ink-light);
  }
  .hero-title em { font-style: italic; font-weight: 400; }
  .hero-actions {
    position: absolute; top: 356px; left: 0; right: 0;
    display: flex; justify-content: center; gap: 15px;
  }
  .hero-actions a {
    height: 41px;
    display: flex; align-items: center; justify-content: center;
    font-size: 10.5px; letter-spacing: 2px;
  }
  .vote-button { width: 160px; background: var(--ink-light); color: var(--button-ink); font-weight: 500; }
  .story-button { width: 168px; border: 1px solid var(--ink-light); color: var(--ink-light); font-weight: 600; }
  .scroll-cue { position: absolute; top: 423px; left: 608px; }
</style>
</head>
<body>
<div class="page">
  <header class="site-header">
    <div class="brand">Lantern Square. Steady Course.</div>
    <nav class="main-nav">
      <a href="#timeline">Timeline</a>
      <a href="#founding">Founding</a>
      <a href="#principles">Principles</a>
      <a href="#data">Data</a>
      <a href="#archive">Archive</a>
    </nav>
    <a class="registry-button" href="#registry">Join Registry</a>
  </header>

  <div class="hero-photo" role="img" aria-label="Black-and-white photograph of a grand historic reading room with arched windows and galleries"></div>

  <section class="hero-content">
    <div class="hero-year">1776</div>
    <h1 class="hero-title">Every generation<br>leaves its mark.<br><em>What will ours be?</em></h1>
    <div class="hero-actions">
      <a class="vote-button" href="#vote">Cast your vote</a>
      <a class="story-button" href="#story">Watch the story</a>
    </div>
    <svg class="scroll-cue" width="16" height="10" viewBox="0 0 16 10" aria-hidden="true">
      <polyline points="1,1 8,8 15,1" fill="none" stroke="#d5d8de" stroke-width="1.2"/>
    </svg>
  </section>
</div>
</body>
</html>
```